Catering Company Website Design

We are working with a bbq catering company in California called Hickory Ember Catering.
Some sites to use for content/competitors and inspiration:
https://19turnips.example
https://brennafoxley.example
https://beyondfeasts.example
https://redbowlmarlow.example (client's favorite)
https://www.dorindasgrill.example (client's favorite)
https://www.thebrightsagekitchen.example
Thank you for taking the time to consider designing a website for us. We are web developers based in Stockton, CA, USA. Most of our projects go through the same process. Understanding this process may help you win a project with us. We custom-code all of our websites in-house. We don’t have any requirements as to what tools you use for your design, but we prefer Figma files. For any design that we label as four-stars, we send it to the client for review. The client picks the final design they want us to use. Once we complete this process, we will continue to show additional clients all the four-star sites and purchase them later. Your designs will have multiple chances to sell. For better chances of success, we ask that you follow these guidelines.
IMAGES:
If you use any images or icons in the design, we ask that you have a link to the asset so we can purchase the image/icon. Most of the designs we submit do not have the customer’s images on them unless they have some great images. Be creative; show us the feeling you are trying to portray with your image choices. Use any royalty-free site you choose. We subscribe to Adobe and mainly use their images, but we can purchase images outside of Adobe.
PLEASE NOTE: we will not submit designs to clients with watermarks on the images.
FONTS:
We ask that you identify the fonts used in the design. This can be done in a message if you want. We typically use Google Fonts and Adobe Fonts.
CONTENT:
We're always open to different content and ideas. We often submit designs with stock images so the client can see our vision. We typically take pictures after the website launch to use their images with our vision. Lorem Ipsum is fine for paragraphs, but we ask that you write the headers in correct English. We want to be able to show the vision and identify the sections of the website.
INSPIRATION:
We typically add a couple of links in the brief of websites we like to help you get started in your design.
REVISIONS:
We do not often ask for revisions of the designs unless we see something in the design that may not appeal to the client. If there are slight changes that we want to make, we do that in the development process.
FEEDBACK:
We rarely give feedback on designs during the design process. We are working on many website projects and do not have the time to provide feedback. We usually respond if your request is well thought out and asks specific questions, but a note asking “feedback, please” usually goes unanswered

```html
<!DOCTYPE html>
<html lang="en">
<head>
<meta charset="utf-8">
<title>Hickory Ember Catering</title>
<link rel="stylesheet" href="https://fonts.googleapis.com/css2?family=Krona+One&family=Lato:wght@400;700;900&display=swap">
<style>
:root{
  --red:#c8171e;
  --red-deep:#a81218;
  --maroon:#5a1512;
  --maroon-dark:#3d0d0b;
  --ink:#2b1a18;
  --text:#5b5b5b;
  --white:#ffffff;
  --display:"Krona One",sans-serif;
  --body:"Lato",sans-serif;
}
*{box-sizing:border-box;margin:0;padding:0}
html,body{width:1200px;height:4147px;overflow:hidden}
body{position:relative;font-family:var(--body);color:var(--ink);background:var(--white)}
svg.edge{position:absolute;left:0;width:1200px;display:block}

/* hero */
.hero{position:absolute;left:0;top:0;width:1200px;height:760px;
  background:radial-gradient(ellipse at 70% 35%,#9a3a1c 0%,#5a1e12 40%,#1e0c08 80%)}
.hero-glow{position:absolute;right:0;top:0;width:700px;height:600px;
  background:radial-gradient(circle at 70% 30%,rgba(255,170,60,.55),rgba(255,120,30,0) 60%)}
.socials{position:absolute;top:12px;left:932px;display:flex;gap:8px}
.soc{width:32px;height:32px;border-radius:50%;border:1.5px solid rgba(255,255,255,.85);display:flex;align-items:center;justify-content:center}
.soc.on{background:var(--red);border-color:var(--red)}
.soc .dot{width:8px;height:8px;border-radius:50%;background:#fff}
.nav{position:absolute;left:111px;top:58px;width:976px;height:86px;background:#fff;border-radius:43px;
  display:flex;align-items:center;justify-content:space-between;padding:0 34px}
.nav ul{list-style:none;display:flex;align-items:center}
.nav li{font-size:16px;font-weight:700;color:var(--ink);padding:0 19px;border-left:1px solid #ddd;line-height:44px}
.nav li:first-child{border-left:0}
.nav li.active{text-decoration:underline;text-decoration-color:var(--red);text-underline-offset:6px}
.brand-badge{position:absolute;left:520px;top:18px;width:160px;height:165px;border-radius:50%;background:#fff;
  display:flex;align-items:center;justify-content:center;text-align:center;font-family:var(--body);
  font-weight:900;font-size:14px;color:var(--ink);line-height:1.2;padding:0 18px}
.hero-copy{position:absolute;left:0;top:296px;width:1200px;text-align:center;color:#fff}
.hero-copy .kicker{font-size:22px;font-weight:700;letter-spacing:.5px}
.hero-copy h1{font-family:var(--display);font-size:48px;line-height:54px;margin-top:18px;font-weight:400}
.btn{display:inline-block;border-radius:26px;font-weight:700;font-size:16px;text-align:center}
.btn-red{background:var(--red);color:#fff}
.btn-white{background:#fff;color:var(--ink)}
.hero-copy .btn{margin-top:22px;width:168px;height:48px;line-height:48px;border-radius:24px;font-size:16px}
.dots{position:absolute;top:619px;left:563px;display:flex;gap:12px}
.dots span{width:10px;height:10px;border-radius:50%;background:rgba(255,255,255,.35)}
.dots span.on{background:#fff}

/* story */
.story{position:absolute;left:0;top:725px;width:1200px;height:590px;background:var(--maroon)}
.story-mark{position:absolute;left:95px;top:160px;width:460px;text-align:center;color:#f3d9d3;font-weight:900;font-size:40px;line-height:1.15}
.story-mark .ring{width:110px;height:110px;border-radius:50%;border:3px solid #e98c7f;margin:0 auto 24px}
.story-copy{position:absolute;left:600px;top:65px;width:490px;color:#fff}
h2.display{font-family:var(--display);font-weight:400;font-size:46px;line-height:1.1}
.story-copy p{font-size:15.5px;line-height:26.5px;text-align:justify;margin-top:16px}
.story-copy h2+p{margin-top:26px}
.story-copy .btn{margin-top:32px;width:142px;line-height:48px}

/* services */
.services-title{position:absolute;top:1468px;left:0;width:1200px;text-align:center;color:var(--maroon-dark)}
.card{position:absolute;top:1575px;width:303px;height:435px;background:#fff;border-radius:22px;box-shadow:0 4px 14px rgba(0,0,0,.15);text-align:center}
.card.featured{outline:2px solid var(--red);outline-offset:-2px}
.card .photo{position:absolute;left:8px;top:7px;right:8px;height:216px;border-radius:18px}
.card h3{position:absolute;top:248px;width:100%;font-size:18px;font-weight:700;color:var(--ink)}
.card p{position:absolute;top:282px;left:22px;right:22px;font-size:15px;line-height:26px;color:var(--text)}
.card .btn{position:absolute;left:81px;bottom:-25px;width:141px;line-height:50px}
.arrow{position:absolute;top:1774px;width:36px;height:36px;border-radius:50%;display:flex;align-items:center;justify-content:center}

/* bbq */
.bbq{position:absolute;left:0;top:2240px;width:1200px;height:680px;background:var(--red)}
.bbq-title{position:absolute;top:2300px;width:1200px;text-align:center;color:#fff}
.process{position:absolute;left:111px;top:2438px;width:490px;color:#fff}
.process h3{font-size:34px;font-weight:700}
.process ul{list-style:none;margin-top:32px}
.process li{position:relative;padding-left:43px;font-size:15.5px;line-height:26.5px;margin-bottom:9px;text-align:justify}
.process li svg{position:absolute;left:0;top:6px}
.process .btn{margin-top:24px;width:210px;line-height:48px}
.bbq-photo{position:absolute;left:659px;top:2422px;width:428px;height:428px;border-radius:50%;
  background:radial-gradient(circle at 45% 55%,#8a3a22 0%,#3a140c 55%,#160806 100%)}
.bbq-photo::after{content:"";position:absolute;inset:13px;border-radius:50%;border:3px solid #fff}

/* blog */
.blog-title{position:absolute;top:3104px;width:1200px;text-align:center;color:var(--maroon-dark)}
.photo{background:linear-gradient(135deg,#5a2a18,#2a100a 60%,#b0501e)}
.blog-main{position:absolute;left:111px;top:3201px;width:446px;height:280px}
.blog-card{position:absolute;left:156px;top:3412px;width:401px;height:193px;background:var(--red);color:#fff;padding:55px 30px 0}
.date{display:inline-block;border-radius:18px;font-size:13px;line-height:34px;padding:0 22px}
.blog-card .date{position:absolute;left:30px;top:-16px;background:#fff;color:var(--ink)}
.blog-card h4{font-size:16px;font-weight:700;line-height:22px}
.blog-card p{font-size:13px;line-height:20px;margin-top:14px}
.blog-card a,.blog-side a{font-weight:700;text-decoration:underline;color:inherit}
.blog-thumb{position:absolute;left:572px;width:250px;height:193px}
.blog-side{position:absolute;left:847px;width:250px}
.blog-side .date{background:var(--red);color:#fff}
.blog-side h4{font-size:16px;font-weight:700;line-height:23px;margin-top:16px;color:var(--ink)}
.blog-side p{font-size:13px;line-height:20px;margin-top:9px;color:var(--ink)}
.blog-side a{color:var(--red)}

/* footer */
.footer{position:absolute;left:0;top:3790px;width:1200px;height:357px;background:var(--maroon)}
.footer-brand{position:absolute;left:111px;top:3900px;width:165px;text-align:center;color:#fff;font-weight:900;font-size:20px;line-height:1.2}
.footer-brand .ring{width:60px;height:60px;border-radius:50%;border:2px solid #fff;margin:0 auto 14px}
.fcol{position:absolute;top:3842px;color:#fff}
.fcol h5{font-size:17px;font-weight:700;margin-bottom:22px}
.fcol ul{list-style:none}
.links li{font-size:14px;line-height:40px;padding-left:33px;position:relative}
.links li::before{content:"";position:absolute;left:0;top:14px;width:13px;height:13px;border-radius:50%;background:var(--red)}
.contact li{position:relative;padding-left:33px;margin-bottom:16px}
.contact li svg{position:absolute;left:0;top:2px}
.contact b{font-size:14px;display:block}
.contact span{font-size:11.5px;line-height:20px}
.signup{width:283px;height:46px;border:2px solid #fff;border-radius:23px;background:#fff;position:relative;display:flex;align-items:center;padding-left:16px;font-size:13px;color:#888}
.signup .btn{position:absolute;right:2px;top:2px;width:102px;line-height:38px;font-size:14px}
.fsoc{display:flex;gap:8px;margin-top:22px}
.fsoc .soc{width:35px;height:35px;background:#fff;border-color:#fff}
.fsoc .soc .dot{background:var(--maroon)}
.fsoc .soc.on{background:var(--red);border-color:var(--red)}
.fsoc .soc.on .dot{background:#fff}
.copy{position:absolute;left:111px;top:4092px;width:976px;border-top:1px solid rgba(255,255,255,.3);padding-top:16px;text-align:center;color:#fff;font-size:13px}
</style>
</head>
<body>

<section class="hero" role="img" aria-label="Photo of sausages and ribs on a flaming grill">
  <div class="hero-glow"></div>
</section>
<svg class="edge" style="top:690px" height="80" viewBox="0 0 1200 80" preserveAspectRatio="none"><path fill="#5a1512" d="M0 10 L60 40 L120 20 L190 45 L260 15 L330 38 L400 12 L480 40 L560 18 L640 42 L720 14 L800 36 L880 10 L960 40 L1040 16 L1120 38 L1200 12 L1200 80 L0 80Z"/></svg>

<div class="socials" aria-label="Social links">
  <span class="soc on"><span class="dot"></span></span>
  <span class="soc"><span class="dot"></span></span>
  <span class="soc"><span class="dot"></span></span>
  <span class="soc"><svg width="16" height="16" viewBox="0 0 16 16"><path d="M1 2h2l2 8h8l2-6H4" fill="none" stroke="#fff" stroke-width="1.6"/><circle cx="6" cy="13" r="1.3" fill="#fff"/><circle cx="12" cy="13" r="1.3" fill="#fff"/></svg></span>
</div>

<nav class="nav">
  <ul><li class="active">HOME</li><li>CATERING</li><li>ABOUT US</li></ul>
  <ul><li>BLOG</li><li>CONTACT</li><li>OFFERS</li></ul>
</nav>
<div class="brand-badge">Hickory Ember Catering</div>

<div class="hero-copy">
  <div class="kicker">BBQ FOR YOUR CAUSE</div>
  <h1>HICKORY EMBER<br>CATERING</h1>
  <span class="btn btn-red">ORDER ONLINE</span>
</div>
<div class="dots"><span></span><span class="on"></span><span></span><span></span></div>

<section class="story">
  <div class="story-mark"><div class="ring"></div>Hickory Ember Catering</div>
  <div class="story-copy">
    <h2 class="display">OUR STORY</h2>
    <p>Lorem ipsum dolor sit amet, consectetur adipiscing elit, sed do eiusmod tempor incididunt ut labore et dolore magna aliqua. Ut enim ad minim veniam, quis nostrud exercitation ullamco laboris nisi ut aliquip ex ea commodo reprehenderit in voluptate velit esse cillum dolore eu fugiat nulla pariaturconsequat.</p>
    <p>Duis aute irure dolor in reprehenderit in voluptate velit esse cillum dolore eu fugiat nulla pariatur. Excepteur sint occaecat cupidatat non proident, sunt in culpa qui officia.</p>
    <span class="btn btn-white">READ MORE</span>
  </div>
</section>
<svg class="edge" style="top:1270px" height="80" viewBox="0 0 1200 80" preserveAspectRatio="none"><path fill="#5a1512" d="M0 0 L1200 0 L1200 12 L1140 40 L1080 22 L1000 50 L920 30 L850 58 L780 28 L700 60 L620 30 L540 62 L470 34 L400 66 L330 38 L260 58 L190 30 L120 52 L60 28 L0 48Z"/></svg>

<h2 class="display services-title">CATERING SERVICES</h2>
<div class="arrow" style="left:37px;background:#e6e6e6"><svg width="12" height="12" viewBox="0 0 12 12"><path d="M8 1 3 6l5 5" fill="none" stroke="#333" stroke-width="2"/></svg></div>
<div class="arrow" style="left:1126px;background:var(--red)"><svg width="12" height="12" viewBox="0 0 12 12"><path d="M4 1l5 5-5 5" fill="none" stroke="#fff" stroke-width="2"/></svg></div>

<article class="card" style="left:111px">
  <div class="photo" role="img" aria-label="Chefs grilling at a catered event"></div>
  <h3>CATERED EVENTS</h3>
  <p>Lorem ipsum dolor sit amet, consectetur adipiscing elit, sed do eiusmod tempor incididunt ut labore et dolorea.</p>
  <span class="btn btn-red">BOOK NOW</span>
</article>
<article class="card featured" style="left:448px">
  <div class="photo" role="img" aria-label="Meat grilling at an outdoor workplace lunch"></div>
  <h3>WORKPLACE DINING</h3>
  <p>Lorem ipsum dolor sit amet, consectetur adipiscing elit, sed do eiusmod tempor incididunt ut labore et dolorea.</p>
  <span class="btn btn-red">BOOK NOW</span>
</article>
<article class="card" style="left:785px">
  <div class="photo" role="img" aria-label="Rack of ribs on a board with sauces"></div>
  <h3>DELIVERY</h3>
  <p>Lorem ipsum dolor sit amet, consectetur adipiscing elit, sed do eiusmod tempor incididunt ut labore et dolorea.</p>
  <span class="btn btn-red">BOOK NOW</span>
</article>

<svg class="edge" style="top:2160px" height="82" viewBox="0 0 1200 82" preserveAspectRatio="none"><path fill="#c8171e" d="M0 50 L70 30 L140 62 L210 34 L290 58 L360 20 L440 50 L520 14 L600 44 L680 10 L760 40 L840 18 L920 46 L1000 8 L1080 40 L1150 22 L1200 36 L1200 82 L0 82Z"/></svg>
<section class="bbq"></section>
<svg class="edge" style="top:2918px" height="80" viewBox="0 0 1200 80" preserveAspectRatio="none"><path fill="#c8171e" d="M0 0 L1200 0 L1200 20 L1130 50 L1060 26 L990 60 L910 30 L840 64 L760 34 L690 58 L610 28 L540 62 L470 34 L390 56 L320 22 L240 50 L170 20 L90 46 L0 18Z"/></svg>
<h2 class="display bbq-title">OUR BBQ</h2>
<div class="process">
  <h3>OUR PROCESS</h3>
  <ul>
    <li><svg width="15" height="15" viewBox="0 0 16 16"><circle cx="8" cy="8" r="8" fill="#fff"/><path d="M5 8h6M8 5l3 3-3 3" fill="none" stroke="#c8171e" stroke-width="2"/></svg>Lorem ipsum dolor sit amet, consectetur adipiscing elit, sed do eiusmod tempor incididunt ut laborea.</li>
    <li><svg width="15" height="15" viewBox="0 0 16 16"><circle cx="8" cy="8" r="8" fill="#fff"/><path d="M5 8h6M8 5l3 3-3 3" fill="none" stroke="#c8171e" stroke-width="2"/></svg>Duis aute irure dolor in reprehenderit in voluptate velit esse cillum dolore eu fugiat.</li>
    <li><svg width="15" height="15" viewBox="0 0 16 16"><circle cx="8" cy="8" r="8" fill="#fff"/><path d="M5 8h6M8 5l3 3-3 3" fill="none" stroke="#c8171e" stroke-width="2"/></svg>Lorem ipsum dolor sit amet, consectetur adipiscing elit, sed do eiusmod tempor incididunt ut laborea.</li>
    <li><svg width="15" height="15" viewBox="0 0 16 16"><circle cx="8" cy="8" r="8" fill="#fff"/><path d="M5 8h6M8 5l3 3-3 3" fill="none" stroke="#c8171e" stroke-width="2"/></svg>Duis aute irure dolor in reprehenderit in voluptate velit esse cillum dolore eu fugiat.</li>
  </ul>
  <span class="btn btn-white">LEARN OUR PROCESS</span>
</div>
<div class="bbq-photo" role="img" aria-label="Steaks searing over an open grill flame"></div>

<h2 class="display blog-title">LATEST BLOG</h2>
<div class="blog-main photo" role="img" aria-label="Steak and vegetables on a flaming grill"></div>
<div class="blog-card">
  <span class="date">10 SEP 2024</span>
  <h4>LOREM IPSUM DOLOR SIT AMET, CON SECTETUR ADIPISEA</h4>
  <p>Lorem ipsum dolor sit amet, consectetur adipiscing elit, sed do eiusmod tempor ut labore... <a>READ MORE</a></p>
</div>
<div class="blog-thumb photo" style="top:3201px" role="img" aria-label="Sauce poured over pulled pork"></div>
<div class="blog-side" style="top:3221px">
  <span class="date">10 SEP 2024</span>
  <h4>LOREM IPSUM DOLOR SIT AME CONSECTETUR ADIPEA</h4>
  <p>Lorem ipsum dolor sit amet, consectetur adipiscing elit sed do... <a>READ MORE</a></p>
</div>
<div class="blog-thumb photo" style="top:3412px" role="img" aria-label="Gloved hand slicing smoked brisket"></div>
<div class="blog-side" style="top:3432px">
  <span class="date">10 SEP 2024</span>
  <h4>LOREM IPSUM DOLOR SIT AME CONSECTETUR ADIPEA</h4>
  <p>Lorem ipsum dolor sit amet, consectetur adipiscing elit sed do... <a>READ MORE</a></p>
</div>

<svg class="edge" style="top:3700px" height="92" viewBox="0 0 1200 92" preserveAspectRatio="none"><path fill="#5a1512" d="M0 60 L60 30 L130 58 L200 20 L280 50 L350 14 L430 46 L510 24 L580 56 L660 18 L740 48 L820 12 L900 44 L970 20 L1050 52 L1120 16 L1200 40 L1200 92 L0 92Z"/></svg>
<footer class="footer"></footer>
<div class="footer-brand"><div class="ring"></div>Hickory Ember Catering</div>
<div class="fcol links" style="left:325px">
  <h5>QUICK LINKS</h5>
  <ul><li>Home</li><li>About Us</li><li>Shop</li><li>Blog</li><li>Magazine</li></ul>
</div>
<div class="fcol contact" style="left:530px;width:240px">
  <h5>CONTACT INFO</h5>
  <ul>
    <li><svg width="12" height="14" viewBox="0 0 12 14"><path d="M6 0a5 5 0 0 0-5 5c0 4 5 9 5 9s5-5 5-9a5 5 0 0 0-5-5z" fill="#c8171e"/><circle cx="6" cy="5" r="2" fill="#5a1512"/></svg><b>ADDRESS:</b><span>465, Lorum Ipsum Dolore Sed Amet, California</span></li>
    <li><svg width="13" height="13" viewBox="0 0 13 13"><path d="M3 0 5 4 3.5 5.5a8 8 0 0 0 4 4L9 8l4 2-1 3C6 13 0 7 0 1z" fill="#c8171e"/></svg><b>PHONE:</b><span>+1 (888) 888 8888</span></li>
    <li><svg width="14" height="11" viewBox="0 0 14 11"><rect width="14" height="11" rx="1" fill="#c8171e"/><path d="M0 1l7 5 7-5" fill="none" stroke="#5a1512" stroke-width="1.4"/></svg><b>EMAIL:</b><span>info@hickoryembercatering.example</span></li>
  </ul>
</div>
<div class="fcol" style="left:805px">
  <h5>NEWSLETTER SIGNUP</h5>
  <div class="signup">Email Address<span class="btn btn-red">SIGN UP</span></div>
  <div class="fsoc"><span class="soc on"><span class="dot"></span></span><span class="soc"><span class="dot"></span></span><span class="soc"><span class="dot"></span></span></div>
</div>
<div class="copy">© 2024 HICKORY EMBER CATERING &nbsp;|&nbsp; All Rights Reserved</div>

</body>
</html>
```